BRIMLOW Pizza and Wraps

We need a website for a new restaurant called BRIMLOW "PIZZA AND WRAPS".
I have attached fonts, background images, logo, images, content etc.
can provide you with what you need to get the website design done fast and easy

I have uploaded more images of the venue and some menu items. let me know if there is anything I need to provide to make your mission clear and easy

Reason: i would like a little time to provide more feedback to designers

Industry/Entity Type

Restaurant

Coding

Coded - Design and coding required

Number of Pages Required

5+ page

Colors

Designer to choose colors to be used in the design.

Requirements
Must have
• PAGES:
• Our Story
• Menu
• Reservations
• Catering & Delivery
• Contact

```html
<!DOCTYPE html>
<html lang="en">
<head>
<meta charset="utf-8">
<title>Brimlow Pizza and Wraps – Reservations, Events &amp; Delivery</title>
<link rel="stylesheet" href="https://fonts.googleapis.com/css2?family=Arvo:wght@700&family=Open+Sans:ital,wght@0,400;0,600;1,400&family=Allura&display=swap">
<style>
  :root {
    --orange: #f7930f;
    --orange-deep: #ef6a1c;
    --white: #ffffff;
    --ink: #4a4a4a;
    --ink-soft: #6d6d6d;
    --leaf: #7fa046;
    --leaf-light: #d9e2c4;
  }
  * { box-sizing: border-box; margin: 0; padding: 0; }
  html, body {
    width: 1200px;
    height: 797px;
    overflow: hidden;
    background: var(--white);
  }
  .page {
    position: relative;
    width: 1200px;
    height: 797px;
    overflow: hidden;
    font-family: "Open Sans", Arial, sans-serif;
    color: var(--ink);
  }
  .dish-photo {
    position: absolute;
    left: 40px;
    top: 0;
    width: 500px;
    height: 78px;
    background: linear-gradient(180deg, var(--leaf) 0%, var(--leaf-light) 55%, #f2f0e6 100%);
  }
  .brush-band {
    position: absolute;
    left: 0;
    top: 60px;
    width: 1200px;
    height: 330px;
  }
  .reservations {
    position: absolute;
    left: 0;
    top: 150px;
    width: 1200px;
    text-align: center;
    color: var(--white);
  }
  .section-title {
    font-family: "Arvo", Georgia, serif;
    font-weight: 700;
    text-transform: uppercase;
    letter-spacing: 1px;
    font-size: 40px;
    line-height: 1.1;
    display: inline-block;
    padding-bottom: 6px;
    border-bottom: 2px solid currentColor;
  }
  .reservations .section-title { font-size: 38px; }
  .note {
    font-style: italic;
    font-size: 14px;
    line-height: 1.55;
    width: 460px;
    margin: 12px auto 0;
  }
  .script-line {
    font-family: "Allura", cursive;
    font-size: 34px;
    line-height: 1;
    margin-top: 4px;
  }
  .events {
    position: absolute;
    left: 0;
    top: 410px;
    width: 1200px;
    text-align: center;
  }
  .events .section-title { color: var(--orange-deep); font-size: 40px; }
  .events-intro {
    width: 860px;
    margin: 18px auto 0;
    font-size: 14px;
    line-height: 1.6;
    color: var(--ink);
  }
  .events-intro .script-line {
    color: var(--ink);
    font-size: 32px;
    margin: 2px 0;
  }
  .services {
    position: absolute;
    left: 170px;
    top: 640px;
    width: 860px;
    display: grid;
    grid-template-columns: 1fr 1fr;
    column-gap: 80px;
  }
  .service-title {
    font-family: "Open Sans", Arial, sans-serif;
    font-weight: 600;
    font-size: 22px;
    letter-spacing: 1px;
    text-transform: uppercase;
    color: var(--ink);
    margin-bottom: 10px;
  }
  .service-text {
    font-size: 14px;
    line-height: 1.6;
    color: var(--ink-soft);
  }
</style>
</head>
<body>
<main class="page">
  <div class="dish-photo" role="img" aria-label="Photo of a fresh salad served on a white plate"></div>

  <svg class="brush-band" viewBox="0 0 1200 330" preserveAspectRatio="none" aria-hidden="true">
    <path fill="#f7930f" d="M0 40 L60 30 L120 44 L210 22 L300 38 L360 26 L430 42 L520 18 L600 36 L690 20 L760 34 L850 16 L930 30 L1010 14 L1090 32 L1150 20 L1200 28 L1200 250 L1160 262 L1120 248 L1070 270 L1010 256 L950 290 L890 268 L820 300 L760 276 L700 296 L620 272 L560 300 L490 278 L420 294 L350 270 L280 288 L220 266 L150 282 L90 262 L30 276 L0 266 Z"/>
  </svg>

  <section class="reservations">
    <h2 class="section-title">Reservations</h2>
    <p class="note">Tables will only be held for 15 minutes past the reservation time. We appreciate your punctuality.</p>
    <p class="script-line">Group bookings</p>
    <p class="note" style="margin-top:2px">All tables of 10 or more guests will have a minimum order requirement of $15 per seat. Please call to make a group booking.</p>
  </section>

  <section class="events">
    <h2 class="section-title">Events &amp; Delivery</h2>
    <div class="events-intro">
      <p>A special event requires a unique experience. Brimlow comes to You! The quality of our cuisine directly to your home with flavour and professionalism to the planning of the menu. Order a single portion and receive it in the comfort of your home or call us for parties, anniversaries and other events.</p>
      <p class="script-line">Let Brimlow cater for your next event</p>
      <p>and make it unforgettable. Create your own unique environment and atmosphere to enjoy our selection of premium quality food and beverages. Enquire about hosting a function.</p>
    </div>
  </section>

  <section class="services">
    <article class="service">
      <h3 class="service-title">Delivery</h3>
      <p class="service-text">Brimlow delivers directly where you want it within our coverage area. This service is available during restaurant hours, every day of the week.</p>
    </article>
    <article class="service">
      <h3 class="service-title">Catering</h3>
      <p class="service-text">Do you have to organize lunches or dinners, business events or private parties? Brimlow will recreate a Mediterranean atmosphere in your home or wherever you prefer.</p>
    </article>
  </section>
</main>
</body>
</html>
```